Neurosurgeon office (Cranial and Spinal diseases)

Need paper itens like:

Business card
Mail
Prescription (A4)
Receipt
Brochure (for informations like disease I treat with place for photo)

My name: Rodrigo Menezes Tavora

PS: need a plain or 3D logo based on my signature

Thanks for all attention !

Preciso de artigos de papelaria:
Cartão de visita
Envelope
Receituário (A4)
Recibo médico
Panfleto (com informações como doenças que trato com lugar para foto)

Meu nome: Rodrigo Menezes Tavora

OBS: Gostaria de um logo baseado na minha rubrica (envio foto abaixo)

Muito obrigado pela atenção !

Hello designers, First, I want to thank you all for helping me with my project. Received some examples, I'm waiting for changes, etc. I had an idea that could do some nice works ... You can try classic style, using soft colors like: White/Black Carolina blue / Air Superiority Blue (http://en.tintopedia.org/wiki/Category:Shades_of_blue) Jungle green (http://en.tintopedia.org/wiki/Category:Shades_of_green) Apricot (http://en.tintopedia.org/wiki/Category:Shades_of_orange) About Logo, you can try logo itself with shapes outside, 3D (like inside a cube or something original) or 2D or a drawing reminding my signature with brain and spine (like brain on C and Spine on F line) or both (like drawings of brain and spine along with the original signature). I'm certain about good works. Would like to receive something original, not a padronized medical paper examples (like using eletrocardiogram, stetoscope, etc ...) ... you can google things that remind my work as brain, neuron, spine, etc ... Thank you all for the attention, certain that someone will achieve my desire for a brilliant work ! Best Regards from Brazil. Rodrigo Tavora PS: going to try to post a JPEG with some examples that you can try on project.

Reason: Received 4 designs under consideration only ... Updated informations today so it's easier to designers to do something that I will like Thanks for all attention ! Best Regards Rodrigo

Reason: No designs that match my search yet

Reason: Waiting for projects

Target Market(s)

Patients with spinal and brain diseases

Industry/Entity Type

Business

Font styles to use
Script
Other font styles liked:
• Times New Roman, Trajan Pro, Palatino LInotype

Colors
33a6d7
add136
3176b5
f9ba93
aaaaaa
f04a50

Requirements
Must have
• The best design I saw on google was like this one ... this is like the logo I want for me ...

https://q7vm3rbtwzk9xe.imgvaultcdn.net/Rb8Kp2TzW4mQx7Lsy_HnVdE91aQ=/fit-in/500x370/http%3A%2F%2Fp4j2wvrkzq8hs.imgvaultcdn.net%2Fdesigns%2F58310947~2b4e90c7a1d3f865b07e12c94f6a3d58b71c0e92-original

Use 2 or more colors with white ... like degradée (different tones of same color)

Nice to have
• Can use logo mixed with RODRIGO TAVORA (and NEUROCIRURGIA below)
Should not have
• Stetoscopes, eletrocradiogram traces

```html
<!DOCTYPE html>
<html lang="en">
<head>
<meta charset="utf-8">
<title>Business Card – Dr. Rodrigo Menezes Tavora</title>
<link rel="stylesheet" href="https://fonts.googleapis.com/css2?family=Open+Sans:wght@400;600;700&display=swap">
<style>
  :root {
    --backdrop: #e6e8ea;
    --card: #ffffff;
    --ink-teal: #0f5877;
    --accent-red: #d94a50;
    --text-grey: #4f5356;
  }
  * { margin: 0; padding: 0; box-sizing: border-box; }
  html, body {
    width: 1200px;
    height: 800px;
    overflow: hidden;
    background: var(--backdrop);
    font-family: "Open Sans", Arial, sans-serif;
  }
  .business-card {
    position: absolute;
    left: 120px;
    top: 130px;
    width: 960px;
    height: 540px;
    background: var(--card);
    box-shadow: 0 6px 24px rgba(0, 0, 0, 0.12);
  }
  .accent-rule {
    position: absolute;
    left: 0;
    top: 0;
    width: 960px;
    height: 540px;
  }
  .accent-rule line {
    stroke: var(--accent-red);
    stroke-width: 5;
    stroke-linecap: round;
  }
  .doctor-name {
    position: absolute;
    right: 200px;
    top: 186px;
    font-size: 31px;
    font-weight: 700;
    font-style: normal;
    color: var(--ink-teal);
    letter-spacing: 0.5px;
    line-height: 1.3;
    white-space: nowrap;
  }
  .specialty {
    position: absolute;
    right: 260px;
    top: 262px;
    font-size: 22px;
    font-weight: 400;
    color: var(--accent-red);
    line-height: 1.3;
  }
  .contact-block {
    position: absolute;
    right: 280px;
    top: 380px;
    text-align: right;
    font-size: 19px;
    font-style: normal;
    line-height: 1.38;
    color: var(--text-grey);
    white-space: nowrap;
  }
  .contact-label {
    font-weight: 700;
    color: var(--ink-teal);
  }
</style>
</head>
<body>
  <article class="business-card">
    <svg class="accent-rule" viewBox="0 0 960 540" aria-hidden="true">
      <line x1="70" y1="248" x2="880" y2="248"/>
    </svg>
    <h1 class="doctor-name">DR.&nbsp; RODRIGO MENEZES TAVORA</h1>
    <p class="specialty">Neurochirurg</p>
    <address class="contact-block">
      Rua das Acácias, 418, Centro Médico Aurora<br>
      13th floor, 20480-112 Rio de Janeiro, RJ, Brasil<br>
      <span class="contact-label">Phone:</span> 55 (21) 3847 1200 · <span class="contact-label">Fax:</span> 55 (21) 3847 1300
    </address>
  </article>
</body>
</html>
```